Borvix Letter head

Borvix is a young and energetic software development consultancy. We spend our time working with clients to turn what ever is in their heads in to software.
We are trying to create an image of a high class software boutique who build class leading bespoke solutions.
We need a sharp letter head that looks great on high quality media.
We like bold colours and distinctive design. So show us what you can do.
Industry/Entity Type
Software
Requirements
Must have
- Our company is based in the UK and are requried to have on the paper somewhere the following information:
* Registered company name: Borvix Ltd
* Registered company number
* VAT registration number
In addition we also want the following:
* An email address
* Telephone number
* Website address
An example of what some pages have in their footer is something like the following:
Borvix Ltd is registered in England and Wales. Reg. no: 4916275
Registered office: 48 Quillmore Road, Harwick Dunshire, HR43PL. Tel: 07442615093
You do not have to use this sentance but please make sure your design incorporates accommodates the requirements for UK based companies

```html
<!DOCTYPE html>
<html lang="en">
<head>
<meta charset="UTF-8">
<title>Borvix Letterhead</title>
<link href="https://fonts.googleapis.com/css2?family=Open+Sans:wght@400;600&display=swap" rel="stylesheet">
<style>
  :root {
    --backdrop: #e9e6e2;
    --paper: #ffffff;
    --brand-red: #c21f2b;
    --brand-red-dark: #a3141f;
    --footer-text: #6a6a6a;
  }
  * { margin: 0; padding: 0; box-sizing: border-box; }
  html, body {
    width: 1200px;
    height: 1000px;
    overflow: hidden;
    background: var(--backdrop);
  }
  .letterhead {
    position: absolute;
    left: 284px;
    top: 29px;
    width: 645px;
    height: 918px;
    background: var(--paper);
    box-shadow: 0 2px 10px rgba(0, 0, 0, 0.12);
    font-family: "Open Sans", Arial, sans-serif;
  }
  .brand-name {
    position: absolute;
    left: 20px;
    top: 22px;
    font-size: 56px;
    font-weight: 600;
    line-height: 1;
    letter-spacing: 1px;
    color: var(--brand-red);
    text-transform: uppercase;
  }
  .footer-rule {
    position: absolute;
    left: 0;
    width: 644px;
    background: var(--brand-red);
  }
  .footer-rule--upper { top: 872px; height: 5px; }
  .footer-rule--lower { top: 880px; height: 4px; background: var(--brand-red-dark); }
  .company-details,
  .contact-details {
    position: absolute;
    top: 887px;
    font-size: 12.5px;
    line-height: 16px;
    color: var(--footer-text);
    white-space: nowrap;
  }
  .company-details { left: 16px; }
  .contact-details { right: 16px; text-align: right; }
</style>
</head>
<body>
  <main class="letterhead">
    <div class="brand-name">Borvix</div>
    <div class="footer-rule footer-rule--upper"></div>
    <div class="footer-rule footer-rule--lower"></div>
    <footer>
      <div class="company-details">
        <p>Borvix Ltd is registered in England and Wales. Reg. no: 4916275</p>
        <p>48 Quillmore Road, Harwick Dunshire, HR43PL.&nbsp; Tel: 07442615093</p>
      </div>
      <div class="contact-details">
        <p>VAT no: GB 284 6193 57</p>
        <p>info@borvix.co.uk&nbsp; borvix.co.uk</p>
      </div>
    </footer>
  </main>
</body>
</html>
```